Tide Harbor Finance Business Cards

Looking for a business card for a new mortgage broking business. Name of the business is Tide Harbor Finance. Purpose of the business is to build trust and strong relationships with clients to then assist them with your mortgage lending needs. Most relationships within the business start off as an enquiry, and then can evolve into a 10+ year relationship, servicing clients from purchasing a new home to then upgrading for their family and even then assisting their children with their first home purchase. Business card should communicate financial security and trust.

Target Market(s)

Targeting professional clients who are looking to build a relationship with a knowledgeable mortgage professional

Industry/Entity Type

Finance - Home Loans

Contact Information for Business Card

Peter Colburn, Director, mobile: 0427 903186, email:peter@tideharborfinance.com.au, website: www.tideharborfinance.com.au

Font styles to use
Sans Serif

Requirements
Must have
• On the front: Must have company logo, contact details as above. On the back: slogan, 'full of choices, free of stress', plus listing services offered: home loans, investment loans, first home buyers, refinancing, car finance

```html
<!DOCTYPE html>
<html lang="en">
<head>
<meta charset="utf-8">
<title>Tide Harbor Finance – Business Cards</title>
<link href="https://fonts.googleapis.com/css2?family=Arimo:wght@400;700&display=swap" rel="stylesheet">
<style>
  :root {
    --navy: #00507a;
    --orange: #f2a200;
    --white: #ffffff;
    --ink: #333333;
    --backdrop: #e6e7e9;
  }
  * { margin: 0; padding: 0; box-sizing: border-box; }
  html, body {
    width: 1032px; height: 1200px; overflow: hidden;
    background: var(--backdrop);
    font-family: "Arimo", Arial, sans-serif;
  }
  .card {
    position: absolute; left: 118px; width: 797px; height: 455px;
    overflow: hidden;
    box-shadow: 8px 10px 14px rgba(0,0,0,0.16);
  }
  .card-front { top: 119px; background: var(--white); }
  .card-back { top: 626px; background: var(--navy); }

  /* front */
  .brand-mark {
    position: absolute; left: 240px; top: 126px;
    width: 110px; height: 110px; border-radius: 50%;
    background: var(--navy);
  }
  .brand-name {
    position: absolute; left: 373px; top: 116px;
    color: var(--navy); font-weight: 700;
    font-size: 46px; line-height: 50px; letter-spacing: -0.5px;
  }
  .front-bands { position: absolute; left: 0; top: 0; width: 797px; height: 455px; }
  .holder {
    position: absolute; left: 524px; top: 328px;
  }
  .holder-name { font-weight: 700; font-size: 29px; color: var(--ink); line-height: 32px; letter-spacing: -0.3px; }
  .holder-role { font-weight: 400; font-size: 27px; color: var(--ink); line-height: 28px; }
  .contact-list {
    position: absolute; left: 38px; top: 341px; list-style: none;
  }
  .contact-list li {
    display: flex; align-items: center; height: 31px;
    color: var(--white); font-size: 22px; letter-spacing: 0.3px;
  }
  .contact-icon { width: 27px; height: 27px; margin-right: 11px; flex: none; }

  /* back */
  .slogan {
    position: absolute; right: 62px; top: 44px; text-align: right; color: var(--white);
  }
  .slogan-light { font-size: 55px; font-weight: 400; line-height: 58px; letter-spacing: -1px; }
  .slogan-bold { font-size: 53px; font-weight: 700; line-height: 60px; letter-spacing: -0.5px; }
  .accent-band {
    position: absolute; left: 0; top: 173px; width: 389px; height: 221px;
    background: var(--orange); border-radius: 0 110px 110px 0;
  }
  .accent-disc {
    position: absolute; left: 176px; top: 185px; width: 197px; height: 197px;
    border-radius: 50%; background: var(--navy);
  }
  .services { position: absolute; left: 427px; top: 178px; }
  .services-title { color: var(--orange); font-weight: 700; font-size: 31px; line-height: 38px; margin-left: 3px; }
  .service-list { list-style: none; }
  .service-list li {
    display: flex; align-items: center; height: 37.5px;
    color: var(--white); font-size: 31px; letter-spacing: -0.2px;
  }
  .tick { width: 25px; height: 16px; margin-right: 6px; flex: none; }
</style>
</head>
<body>

<section class="card card-front">
  <div class="brand-mark"></div>
  <div class="brand-name">TIDE<br>HARBOR<br>FINANCE</div>

  <svg class="front-bands" viewBox="0 0 797 455" aria-hidden="true">
    <rect x="0" y="318" width="797" height="6" fill="var(--orange)"/>
    <polygon points="485,318 797,318 797,388 496,388" fill="var(--orange)"/>
    <polygon points="0,330 440,330 453,393 797,393 797,455 0,455" fill="var(--navy)"/>
    <g fill="var(--navy)">
      <ellipse cx="470" cy="355" rx="6.5" ry="8"/>
      <path d="M456 375 q2 -10 14 -10 q12 0 14 10 z"/>
    </g>
  </svg>

  <ul class="contact-list">
    <li>
      <svg class="contact-icon" viewBox="0 0 28 28" aria-hidden="true">
        <circle cx="14" cy="14" r="12.5" fill="none" stroke="var(--orange)" stroke-width="1.5"/>
        <circle cx="14" cy="14" r="9.5" fill="var(--orange)"/>
        <rect x="8.5" y="10" width="11" height="8" fill="none" stroke="var(--navy)" stroke-width="1.2"/>
        <path d="M8.5 10 L14 15 L19.5 10" fill="none" stroke="var(--navy)" stroke-width="1.2"/>
      </svg>
      0427 903186
    </li>
    <li>
      <svg class="contact-icon" viewBox="0 0 28 28" aria-hidden="true">
        <circle cx="14" cy="14" r="12.5" fill="none" stroke="var(--orange)" stroke-width="1.5"/>
        <circle cx="14" cy="14" r="9.5" fill="var(--orange)"/>
        <path d="M14 21 C10 16 9.5 14 9.5 12.5 a4.5 4.5 0 0 1 9 0 C18.5 14 18 16 14 21 z" fill="none" stroke="var(--navy)" stroke-width="1.3"/>
        <circle cx="14" cy="12.5" r="1.6" fill="var(--navy)"/>
      </svg>
      peter@tideharborfinance.com.au
    </li>
    <li>
      <svg class="contact-icon" viewBox="0 0 28 28" aria-hidden="true">
        <circle cx="14" cy="14" r="12.5" fill="none" stroke="var(--orange)" stroke-width="1.5"/>
        <circle cx="14" cy="14" r="9.5" fill="var(--orange)"/>
        <g fill="none" stroke="var(--navy)" stroke-width="1">
          <circle cx="14" cy="14" r="5.5"/>
          <ellipse cx="14" cy="14" rx="2.5" ry="5.5"/>
          <line x1="8.5" y1="14" x2="19.5" y2="14"/>
          <line x1="9.3" y1="11.3" x2="18.7" y2="11.3"/>
          <line x1="9.3" y1="16.7" x2="18.7" y2="16.7"/>
        </g>
      </svg>
      www.tideharborfinance.com.au
    </li>
  </ul>

  <div class="holder">
    <div class="holder-name">PETER COLBURN</div>
    <div class="holder-role">Director</div>
  </div>
</section>

<section class="card card-back">
  <div class="slogan">
    <div class="slogan-light">FULL OF CHOICES,</div>
    <div class="slogan-bold">FREE OF STRESS</div>
  </div>

  <div class="accent-band"></div>
  <div class="accent-disc"></div>

  <div class="services">
    <div class="services-title">Services Offered:</div>
    <ul class="service-list">
      <li><svg class="tick" viewBox="0 0 25 16" aria-hidden="true"><path d="M1 8 L8 14 L24 2 L8 10 Z" fill="var(--orange)"/></svg>Home Loans</li>
      <li><svg class="tick" viewBox="0 0 25 16" aria-hidden="true"><path d="M1 8 L8 14 L24 2 L8 10 Z" fill="var(--orange)"/></svg>Investment Loans</li>
      <li><svg class="tick" viewBox="0 0 25 16" aria-hidden="true"><path d="M1 8 L8 14 L24 2 L8 10 Z" fill="var(--orange)"/></svg>First Home Buyers</li>
      <li><svg class="tick" viewBox="0 0 25 16" aria-hidden="true"><path d="M1 8 L8 14 L24 2 L8 10 Z" fill="var(--orange)"/></svg>Refinancing</li>
      <li><svg class="tick" viewBox="0 0 25 16" aria-hidden="true"><path d="M1 8 L8 14 L24 2 L8 10 Z" fill="var(--orange)"/></svg>&nbsp;Car Finance</li>
    </ul>
  </div>
</section>

</body>
</html>
```